Owner of Clinical Testing Lab/. Pixel Harbor Logo completed. Need Matching business Cards

Im the owner of and need cards for business. Colors fonts and logo already purchased through pixel harbor and have the source files. Like to keep same color format , Include logo one side. My Name Address of Lab. My cell number, Lab telephone number and website address. Want to keep simple.

Target Market(s)

Customers

Industry/Entity Type

HealthCare

Contact Information for Business Card

Dr. Corisande Threlkeld Ph.D. Address: QVT Foundry Campus 4417 Foundry Campus Loop Building 2600 Room 314. Baton Rouge LA 70931. Phone : 555.317.0942

Requirements
Must have
• Logo - Color same

```html
<!DOCTYPE html>
<html lang="en">
<head>
<meta charset="utf-8">
<title>Bondline Laboratories – Business Card</title>
<link rel="stylesheet" href="https://fonts.googleapis.com/css2?family=Mulish:ital,wght@0,400;0,600;1,800&display=swap">
<style>
  :root {
    --navy: #0d4a7e;
    --navy-deep: #0a3d6b;
    --teal: #5cc3a8;
    --ink: #4a4a4a;
    --paper: #ffffff;
    --backdrop: #e9ecef;
  }
  * { box-sizing: border-box; margin: 0; padding: 0; }
  html, body { width: 1200px; height: 900px; overflow: hidden; }
  body {
    background: var(--backdrop);
    font-family: "Mulish", sans-serif;
    display: flex;
    flex-direction: column;
    align-items: center;
    justify-content: center;
    gap: 60px;
  }
  .card {
    position: relative;
    width: 630px;
    height: 360px;
    border-radius: 4px;
    overflow: hidden;
    box-shadow: 0 10px 30px rgba(0,0,0,.18);
  }
  /* front side */
  .card-front { background: var(--paper); }
  .card-front .wave { position: absolute; inset: 0; width: 100%; height: 100%; }
  .brand {
    position: absolute;
    left: 40px;
    top: 92px;
    width: 230px;
    display: flex;
    align-items: center;
    gap: 12px;
    color: var(--navy);
    font-weight: 600;
    font-size: 26px;
    line-height: 1.15;
    letter-spacing: .02em;
  }
  .brand-dot {
    flex: none;
    width: 18px; height: 18px;
    border-radius: 50%;
    background: var(--navy);
  }
  .divider {
    position: absolute;
    left: 292px;
    top: 62px;
    width: 2px;
    height: 148px;
    background: var(--navy);
  }
  .details {
    position: absolute;
    left: 312px;
    top: 60px;
    right: 26px;
    color: var(--ink);
  }
  .holder {
    color: var(--navy);
    font-weight: 800;
    font-style: italic;
    font-size: 19px;
    margin-bottom: 8px;
  }
  .address { font-size: 13px; line-height: 1.45; margin-bottom: 8px; }
  .contact-list { list-style: none; font-size: 13px; line-height: 1.6; }
  .contact-list li { display: flex; align-items: center; gap: 7px; }
  .contact-list svg { width: 12px; height: 12px; fill: var(--teal); flex: none; }

  /* back side */
  .card-back {
    background: var(--navy);
    display: flex;
    align-items: center;
    justify-content: center;
    gap: 16px;
  }
  .card-back .brand-back {
    color: var(--paper);
    font-weight: 600;
    font-size: 38px;
    letter-spacing: .03em;
  }
  .card-back .brand-dot { width: 24px; height: 24px; background: var(--paper); }
</style>
</head>
<body>

  <section class="card card-front" aria-label="Business card front">
    <svg class="wave" viewBox="0 0 630 360" preserveAspectRatio="none" aria-hidden="true">
      <path d="M0 290 C 150 300, 330 360, 630 345 L630 360 L0 360 Z" fill="var(--navy)"/>
      <path d="M0 282 C 160 286, 330 345, 600 352" fill="none" stroke="var(--teal)" stroke-width="4"/>
    </svg>

    <div class="brand">
      <span class="brand-dot"></span>
      <span>Bondline Laboratories</span>
    </div>

    <div class="divider"></div>

    <div class="details">
      <p class="holder">Dr. Corisande Threlkeld Ph.D</p>
      <p class="address">QVT Foundry Campus 4417 Foundry Campus Loop Building 2600 Room 314<br>Baton Rouge LA 70931</p>
      <ul class="contact-list">
        <li>
          <svg viewBox="0 0 24 24" aria-hidden="true"><path d="M6.6 10.8a15.1 15.1 0 0 0 6.6 6.6l2.2-2.2a1 1 0 0 1 1-.25 11.4 11.4 0 0 0 3.6.57 1 1 0 0 1 1 1V20a1 1 0 0 1-1 1A17 17 0 0 1 3 4a1 1 0 0 1 1-1h3.5a1 1 0 0 1 1 1c0 1.25.2 2.45.57 3.57a1 1 0 0 1-.25 1z"/></svg>
          555.317.0942
        </li>
        <li>
          <svg viewBox="0 0 24 24" aria-hidden="true"><path d="M2 5h20v14H2z M2 5l10 8 10-8" /></svg>
          info@bondlinelabs.com
        </li>
        <li>
          <svg viewBox="0 0 24 24" aria-hidden="true"><circle cx="12" cy="12" r="10"/></svg>
          www.bondlinelabs.com
        </li>
      </ul>
    </div>
  </section>

  <section class="card card-back" aria-label="Business card back">
    <span class="brand-dot"></span>
    <span class="brand-back">Bondline Laboratories</span>
  </section>

</body>
</html>
```